Jasmine Gin Bottle Label

I need a label design for a gin bottle. We are a small, farm based distillery producing hand crafted spirits. I've attached a mock-up of a wrap label on the bottle we use. I'd like to see imagery of Jasmin flower(s) in the label.
Our logo is attached.

Target Market(s)

Adults of legal drinking age who enjoy quality spirits

Industry/Entity Type

Alcoholic beverage production

Requirements
Must have
• Logo displayed. Details on label as follows: 750 mL 40% alc/vol
Nice to have
• I like contrast is a design

```html
<!DOCTYPE html>
<html lang="en">
<head>
<meta charset="utf-8">
<title>Jasmin Gin Label</title>
<link rel="stylesheet" href="https://fonts.googleapis.com/css2?family=Oswald:wght@400;600&family=Kaushan+Script&family=EB+Garamond:wght@400&display=swap">
<style>
  :root {
    --page: #f4f3f0;
    --cream: #e6e3dc;
    --cream-deep: #d9d5cc;
    --tan: #b08a63;
    --panel: #232323;
    --panel-soft: #2b2b2b;
    --ink-light: #e9e7e2;
    --ink-dark: #2a2a2a;
    --leaf: #8cc47a;
    --petal: #f7f7f3;
  }
  * { margin: 0; padding: 0; box-sizing: border-box; }
  html, body {
    width: 900px;
    height: 1200px;
    overflow: hidden;
    background: var(--page);
  }
  .canvas {
    position: relative;
    width: 900px;
    height: 1200px;
  }
  .label {
    position: absolute;
    left: 50px;
    top: 155px;
    width: 800px;
    height: 889px;
    display: flex;
    box-shadow: 0 10px 30px rgba(0,0,0,0.12);
  }
  .botanical-panel {
    width: 267px;
    height: 100%;
    background: var(--cream);
  }
  .botanical-art {
    width: 100%;
    height: 100%;
    background:
      radial-gradient(ellipse 38% 14% at 68% 24%, var(--petal), transparent 75%),
      radial-gradient(ellipse 40% 13% at 45% 66%, var(--petal), transparent 75%),
      radial-gradient(ellipse 30% 22% at 35% 38%, rgba(140,196,122,0.55), transparent 75%),
      linear-gradient(180deg, var(--cream) 0%, var(--cream-deep) 100%);
  }
  .tan-stripe { width: 9px; background: var(--tan); }
  .tan-stripe.thin { width: 5px; }
  .brand-panel {
    position: relative;
    width: 486px;
    height: 100%;
    background: linear-gradient(180deg, var(--panel-soft), var(--panel));
    color: var(--ink-light);
    text-align: center;
  }
  .edge-strip { width: 33px; background: var(--cream-deep); }

  .brand-mark {
    position: absolute;
    top: 140px;
    left: 0;
    right: 0;
    display: flex;
    flex-direction: column;
    align-items: center;
    gap: 14px;
  }
  .brand-dot {
    width: 18px;
    height: 18px;
    border-radius: 50%;
    border: 2px solid var(--ink-light);
  }
  .brand-name {
    font-family: 'Oswald', sans-serif;
    font-weight: 400;
    font-size: 30px;
    letter-spacing: 4px;
    text-transform: uppercase;
    color: var(--ink-light);
    line-height: 1.2;
  }
  .product-name {
    position: absolute;
    top: 378px;
    left: 0;
    right: 0;
    font-family: 'Oswald', sans-serif;
    font-weight: 600;
    font-size: 148px;
    line-height: 1;
    letter-spacing: 1px;
    color: var(--ink-light);
  }
  .product-type {
    position: absolute;
    top: 570px;
    left: 0;
    right: 0;
    font-family: 'Kaushan Script', cursive;
    font-size: 92px;
    line-height: 1.2;
    color: var(--ink-light);
  }
  .spec-box {
    position: absolute;
    left: 68px;
    top: 757px;
    width: 371px;
    height: 78px;
    background: var(--cream-deep);
    border: 2px solid var(--cream-deep);
    outline: 2px solid #9a968f;
    outline-offset: -7px;
    display: flex;
    justify-content: space-between;
    align-items: center;
    padding: 0 28px;
    font-family: 'EB Garamond', serif;
    font-size: 27px;
    color: var(--ink-dark);
  }
</style>
</head>
<body>
<div class="canvas">
  <div class="label">
    <div class="botanical-panel">
      <div class="botanical-art" role="img" aria-label="Illustration of white jasmine blossoms with green leaves and buds on a branch"></div>
    </div>
    <div class="tan-stripe"></div>
    <div class="brand-panel">
      <div class="brand-mark">
        <span class="brand-dot"></span>
        <span class="brand-name">Stonebrook Distillery</span>
      </div>
      <h1 class="product-name">JASMIN</h1>
      <p class="product-type">Gin</p>
      <div class="spec-box">
        <span class="spec-volume">750 ml</span>
        <span class="spec-abv">40% alc/vol</span>
      </div>
    </div>
    <div class="tan-stripe thin"></div>
    <div class="edge-strip"></div>
  </div>
</div>
</body>
</html>
```